Bluewren Business Cards

Name Tomas Velikor
Title Mortgage Originator
Phone (800) 641-2705 x32
Direct (571) 362-8104
Email tvelikor@bluewrenhomeloans.example
NMLS #3804427
Name Lien Vo
Title Mortgage Originator
Location (800) 641-2705 x55
Direct (440) 296-5081
Email lvo@bluewrenhomeloans.example
NMLS #3719046
Name Solomon Ked-Ravi
Title Mortgage Originator
Location (800) 641-2705 x56
Direct (202) 374-6019
Email skedravi@bluewrenhomeloans.example
NMLS #3748510
Name Roselle Dunfield
Title Mortgage Originator
Location (800) 641-2705 x57
Direct (240) 538-2274
Email rdunfield@bluewrenhomeloans.example
NMLS #3692384
Name Dana Whitcombe
Title Mortgage Originator
Location (800) 641-2705 x58
Direct (540) 681-3926
Email dwhitcombe@bluewrenhomeloans.example
NMLS #3657019
Name Idris Holt
Title Mortgage Originator
Location (800) 641-2705 x59
Direct (240) 163-8852
Email iholt@bluewrenhomeloans.example
NMLS #3781462
Name Zora Lund
Title Mortgage Originator
Location (800) 641-2705 x60
Direct (202) 449-2637
Email zora@zorafindshomes.example
NMLS #3795038
Contact Information for Business Card
Name Tomas Velikor Title Mortgage Originator Phone (800) 641-2705 x32 Direct (571) 362-8104 Email tvelikor@bluewrenhomeloans.example NMLS #3804427 Name Lien Vo Title Mortgage Originator Location (800) 641-2705 x55 Direct (440) 296-5081 Email lvo@bluewrenhomeloans.example NMLS #3719046 Name Solomon Ked-Ravi Title Mortgage Originator Location (800) 641-2705 x56 Direct (202) 374-6019 Email skedravi@bluewrenhomeloans.example NMLS #3748510 Name Roselle Dunfield Title Mortgage Originator Location (800) 641-2705 x57 Direct (240) 538-2274 Email rdunfield@bluewrenhomeloans.example NMLS #3692384 Name Dana Whitcombe Title Mortgage Originator Location (800) 641-2705 x58 Direct (540) 681-3926 Email dwhitcombe@bluewrenhomeloans.example NMLS #3657019 Name Idris Holt Title Mortgage Originator Location (800) 641-2705 x59 Direct (240) 163-8852 Email iholt@bluewrenhomeloans.example NMLS #3781462 Name Zora Lund Title Mortgage Originator Location (800) 641-2705 x60 Direct (202) 449-2637 Email zora@zorafindshomes.example NMLS #3795038

```html
<!DOCTYPE html>
<html lang="en">
<head>
<meta charset="utf-8">
<title>Bluewren Business Card – Zora Lund</title>
<link rel="stylesheet" href="https://fonts.googleapis.com/css2?family=Playfair+Display:wght@400&family=Montserrat:wght@500&family=Lato:wght@400;700&display=swap">
<style>
  :root {
    --stage: #808080;
    --card-dark: #151515;
    --card-mid: #262626;
    --gold: #f7c53c;
    --white: #ffffff;
    --ink: #111111;
    --ring: #4a4a4a;
    --photo-light: #e4e2e1;
    --photo-mid: #b9a89c;
  }
  * { margin: 0; padding: 0; box-sizing: border-box; }
  html, body {
    width: 1200px; height: 1000px; overflow: hidden;
    background: var(--stage);
  }
  .business-card {
    position: absolute; left: 26px; top: 172px;
    width: 1149px; height: 656px;
    border-radius: 30px;
    background: radial-gradient(ellipse at 50% 40%, var(--card-mid) 0%, var(--card-dark) 75%);
    overflow: hidden;
  }
  .portrait {
    position: absolute; left: 205px; top: 136px;
    width: 228px; height: 228px; border-radius: 50%;
    border: 6px solid var(--ring);
    background: radial-gradient(circle at 50% 35%, var(--photo-light) 0%, var(--photo-light) 45%, var(--photo-mid) 100%);
  }
  .identity {
    position: absolute; left: 119px; top: 382px; width: 400px;
    text-align: center;
  }
  .name {
    font-family: "Playfair Display", serif;
    font-size: 62px; font-weight: 400; line-height: 1;
    color: var(--white);
  }
  .name .surname { color: var(--gold); }
  .title {
    margin-top: 16px;
    font-family: "Montserrat", sans-serif;
    font-size: 25px; font-weight: 500; letter-spacing: 1px;
    color: var(--white);
  }
  .contact {
    position: absolute; left: 692px; top: 210px; width: 340px;
    text-align: center;
    font-family: "Lato", sans-serif; color: var(--white);
  }
  .contact-icons { display: block; margin: 0 auto 14px; }
  .contact-line { font-size: 31px; line-height: 50px; }
  .contact-line.email { font-size: 29px; line-height: 44px; }
  .nmls {
    display: inline-block; margin-top: 36px;
    width: 260px; height: 47px; line-height: 47px;
    border-radius: 24px; background: var(--gold);
    color: var(--ink); font-weight: 700; font-size: 25px;
  }
</style>
</head>
<body>
  <main class="business-card">
    <div class="portrait" role="img" aria-label="Portrait photo of Zora Lund"></div>

    <div class="identity">
      <h1 class="name">Zora <span class="surname">Lund</span></h1>
      <p class="title">MORTGAGE ORIGINATOR</p>
    </div>

    <div class="contact">
      <svg class="contact-icons" width="222" height="38" viewBox="0 0 222 38" fill="none" stroke="var(--gold)" stroke-width="2.5" stroke-linecap="round" stroke-linejoin="round" aria-hidden="true">
        <line x1="2" y1="19" x2="42" y2="19"/>
        <line x1="182" y1="19" x2="220" y2="19"/>
        <rect x="48" y="2" width="36" height="34" rx="5"/>
        <rect x="60" y="9" width="12" height="20" rx="2"/>
        <line x1="64" y1="25" x2="68" y2="25"/>
        <rect x="93" y="2" width="36" height="34" rx="5"/>
        <path d="M100 17 q11 -8 22 0 l-2 3 h-4 l-1 -3 h-8 l-1 3 h-4 z"/>
        <rect x="103" y="21" width="16" height="9" rx="1"/>
        <rect x="138" y="2" width="36" height="34" rx="5"/>
        <path d="M145 19 l22 -10 l-6 21 l-5 -7 z M156 23 l11 -14"/>
      </svg>
      <p class="contact-line">(800) 641-2705 x60</p>
      <p class="contact-line">(202) 449-2637</p>
      <p class="contact-line email">zora@zorafindshomes.example</p>
      <span class="nmls">NMLS #3795038</span>
    </div>
  </main>
</body>
</html>
```